Bright Towns Alliance PowerPoint Design Template and Sample Deck

The Bright Towns Alliance is an international organization that seeks to improve the livability, workability and sustainability of the world’s cities.
We seek a versatile PowerPoint design template with 10 slide types plus a “self-documenting” sample deck. Your design will be used in keynote speeches and workshops around the world.
After the contest is completed, we will ask the winning designer to add 10-20 additional slide types for $75 per slide. We also seek a long-term relationship whereby we can request “custom” slides and/or ask the designer to touch up the slides we build to make them better.
FILES. We have uploaded several files:
1. BRIGHT TOWNS ALLIANCE DESIGN CONTEST NOTES.docx with full instructions.
2. PALETTE. Shows our official colors.
3 LOGOS. Several individual files with different variations of our logo. Some with our motto, some without.
2. SAMPLE SLIDES. Because we were unable to successfully upload our sample deck, we are making it available via this FileCrate link:
https://www.filecrate-example.net/s/k7qvmr2tn8wzd4h/The%20Bright%20Towns%20Alliance%20Design%20Contest%20Notes.docx?dl=0
Target Market(s)
Mayors, department heads, CIOs, senior executives from technology companies
Industry/Entity Type
Information Technology
Colors
Designer to choose colors to be used in the design.
Requirements
Must have
- Please see uploaded Word document for requirements, nice to haves and should not haves and uploaded palette for color preferences.
Nice to have
- see above
Should not have
- see above

```html
<!DOCTYPE html>
<html lang="en">
<head>
<meta charset="utf-8">
<title>Bright Towns Alliance – Template and Sample Deck</title>
<link href="https://fonts.googleapis.com/css2?family=Open+Sans:wght@400;600;700;800&display=swap" rel="stylesheet">
<style>
:root{
  --stage:#cdbfae;
  --navy:#10295a;
  --blue:#1f5aa8;
  --sky:#3f86d0;
  --orange:#f39a1e;
  --purple:#7a3fa6;
  --green:#5f9e37;
  --red:#e9532b;
  --pink:#c4317a;
  --gray:#7a7a7a;
  --ink:#3a3a3a;
  --muted:#9a9a9a;
  --line:#d9dde3;
  --white:#ffffff;
}
*{box-sizing:border-box;margin:0;padding:0}
html,body{width:1200px;height:4491px;overflow:hidden}
body{background:var(--stage);font-family:"Open Sans",Arial,sans-serif;color:var(--ink);position:relative}
.slide{position:absolute;width:346px;height:195px;overflow:hidden;background:var(--white);box-shadow:0 3px 8px rgba(0,0,0,.28)}
.c1{left:73px}.c2{left:450px}.c3{left:820px}
.footer{position:absolute;left:0;right:0;bottom:0;height:15px;background:var(--navy);display:flex;justify-content:space-between;align-items:center;padding:0 10px;color:var(--white);font-size:6.5px}
.footer .brand{font-weight:700;font-size:7px}
.footer .meta{opacity:.7;font-size:5px}
.title{position:absolute;top:10px;left:0;right:0;text-align:center;font-weight:700;font-size:11px;color:var(--blue);white-space:nowrap}
.title::after{content:"";display:block;width:16px;height:1.5px;background:var(--orange);margin:4px auto 0}
.title.left{text-align:left;left:20px}
.title.left::after{margin-left:0}
.title.light{color:var(--white)}
.section{color:var(--white)}
.section .label{position:absolute;right:24px;top:46%;font-size:9px;font-weight:600;white-space:nowrap;text-align:right}
.section .label small{display:block;font-size:5px;opacity:.7;font-weight:400;margin-top:2px}
.lockup{position:absolute;display:flex;align-items:center;gap:5px;font-size:11px;font-weight:700;color:var(--blue);white-space:nowrap}
.lockup .sq{width:8px;height:8px;background:var(--blue)}
.photo{position:absolute}
.ph-crowd{background:linear-gradient(160deg,#6b7079,#3b3f47 60%,#8a8c90)}
.ph-crowd-c{background:linear-gradient(160deg,#7d8796,#48566b 55%,#a8b2bf)}
.ph-city{background:linear-gradient(180deg,#2c5a9c,#173a74 70%,#0f2a5a)}
.ph-portrait{background:linear-gradient(90deg,#2d4372 0%,#3f5e93 45%,#b08a76 75%,#8c6a5a)}
.ph-pink{background:linear-gradient(160deg,#d1427f,#a32565)}
.ph-skyline{background:linear-gradient(180deg,#a9d17f,#5f9e37)}
.ph-map{background:linear-gradient(180deg,#e3e6ea,#cfd3d8)}
.ph-map.dark{background:linear-gradient(180deg,#2a4578,#1d3568)}
.txt{position:absolute;font-size:5px;line-height:1.5;color:var(--muted)}
.txt.w{color:rgba(255,255,255,.85)}
.banner{position:absolute;background:rgba(16,41,90,.88);color:var(--white);font-size:8px;font-weight:700;text-align:center;padding:5px 4px;white-space:nowrap}
.banner.blue{background:var(--blue)}
.big{font-weight:800;color:var(--white)}
.accent{color:var(--orange)}
.stat{position:absolute;color:var(--white);text-align:center;width:60px}
.stat b{display:block;font-size:12px;font-weight:700}
.stat span{font-size:4.5px;opacity:.85}
.tbl{position:absolute;border-collapse:collapse;font-size:4.5px;color:var(--ink)}
.tbl th{background:var(--blue);color:var(--white);padding:3px 6px;text-align:left}
.tbl td{padding:3px 6px;border-bottom:1px solid var(--line)}
.tbl tr:nth-child(even) td{background:#eef1f5}
svg{position:absolute;left:0;top:0}
</style>
</head>
<body>

<!-- Row 1 -->
<section class="slide c1" style="top:24px">
  <div class="photo ph-city" style="inset:0" role="img" aria-label="City skyline photograph in blue tones"></div>
  <div class="big" style="position:absolute;left:30px;top:44px;font-size:17px">The world is <span class="accent">changing</span></div>
  <div class="txt w" style="left:40px;top:70px;font-style:italic">“The biggest shift in economic activity in history”<br>— Add source name</div>
  <div class="footer"><span class="brand">Bright Towns Alliance</span><span class="meta">Add footer note</span></div>
</section>
<section class="slide c2 section" style="top:24px;background:linear-gradient(135deg,#8a4db5,var(--purple))">
  <div class="label">1 Progressive Agenda<small>Slide Notes</small></div>
</section>
<section class="slide c3" style="top:24px">
  <div class="title">Progressive Agenda</div>
  <svg width="346" height="195" viewBox="0 0 346 195">
    <rect x="70" y="120" width="36" height="30" fill="#5f9e37"/><rect x="114" y="105" width="36" height="45" fill="#7a3fa6"/>
    <rect x="158" y="90" width="36" height="60" fill="#f39a1e"/><rect x="202" y="75" width="36" height="75" fill="#3f86d0"/>
    <rect x="246" y="58" width="36" height="92" fill="#1f5aa8"/>
  </svg>
  <div class="footer"><span class="brand">Bright Towns Alliance</span><span class="meta">Add footer note</span></div>
</section>

<!-- Row 2 -->
<section class="slide c1" style="top:245px">
  <div class="title">Progressive Agenda</div>
  <svg width="346" height="195" viewBox="0 0 346 195">
    <path d="M30 80h48l8 10-8 10H30z" fill="#f39a1e"/><path d="M88 80h48l8 10-8 10H88z" fill="#7a3fa6"/>
    <path d="M146 80h48l8 10-8 10h-48z" fill="#1f5aa8"/><path d="M204 80h48l8 10-8 10h-48z" fill="#5f9e37"/>
    <path d="M262 80h48l8 10-8 10h-48z" fill="#3f86d0"/>
    <circle cx="56" cy="130" r="9" fill="none" stroke="#f39a1e" stroke-width="2"/><circle cx="114" cy="130" r="9" fill="none" stroke="#7a3fa6" stroke-width="2"/>
    <circle cx="172" cy="130" r="9" fill="none" stroke="#1f5aa8" stroke-width="2"/><circle cx="230" cy="130" r="9" fill="none" stroke="#5f9e37" stroke-width="2"/>
    <circle cx="288" cy="130" r="9" fill="none" stroke="#3f86d0" stroke-width="2"/>
  </svg>
  <div class="txt" style="left:30px;top:62px">Step one</div><div class="txt" style="left:146px;top:62px">Step three</div><div class="txt" style="left:262px;top:62px">Step five</div>
  <div class="footer"><span class="brand">Bright Towns Alliance</span><span class="meta">Add footer note</span></div>
</section>
<section class="slide c2" style="top:245px">
  <div class="title">Progressive Agenda</div>
  <svg width="346" height="195" viewBox="0 0 346 195">
    <rect x="60" y="50" width="18" height="18" fill="#1f5aa8"/><rect x="60" y="85" width="18" height="18" fill="#f39a1e"/><rect x="60" y="120" width="18" height="18" fill="#5f9e37"/>
    <rect x="190" y="50" width="18" height="18" fill="#7a3fa6"/><rect x="190" y="85" width="18" height="18" fill="#3f86d0"/><rect x="190" y="120" width="18" height="18" fill="#e9532b"/>
  </svg>
  <div class="txt" style="left:84px;top:55px">Add your topic here</div><div class="txt" style="left:84px;top:90px">Add your topic here</div><div class="txt" style="left:84px;top:125px">Add your topic here</div>
  <div class="txt" style="left:214px;top:55px">Add your topic here</div><div class="txt" style="left:214px;top:90px">Add your topic here</div><div class="txt" style="left:214px;top:125px">Add your topic here</div>
  <div class="footer"><span class="brand">Bright Towns Alliance</span><span class="meta">Add footer note</span></div>
</section>
<section class="slide c3" style="top:245px">
  <div class="title">Progressive Agenda</div>
  <svg width="346" height="195" viewBox="0 0 346 195">
    <rect x="20" y="140" width="34" height="40" fill="#5f9e37"/><rect x="54" y="120" width="34" height="60" fill="#7a3fa6"/>
    <rect x="88" y="100" width="34" height="80" fill="#f39a1e"/><rect x="122" y="80" width="34" height="100" fill="#3f86d0"/>
    <rect x="156" y="58" width="34" height="122" fill="#1f5aa8"/>
  </svg>
  <div class="lockup" style="left:210px;top:52px"><span class="sq"></span>Bright Towns Alliance</div>
  <div class="txt" style="left:210px;top:80px;width:120px">Add your agenda point here<br>Add your agenda point here<br>Add your agenda point here</div>
  <div class="footer"><span class="brand">Bright Towns Alliance</span><span class="meta">Add footer note</span></div>
</section>

<!-- Row 3 -->
<section class="slide c1" style="top:465px">
  <div class="title">Progressive Agenda</div>
  <div class="lockup" style="left:20px;top:52px"><span class="sq"></span>Bright Towns Alliance</div>
  <svg width="346" height="195" viewBox="0 0 346 195">
    <rect x="40" y="140" width="30" height="40" fill="#5f9e37"/><rect x="70" y="122" width="30" height="58" fill="#7a3fa6"/>
    <rect x="100" y="104" width="30" height="76" fill="#f39a1e"/><rect x="130" y="86" width="30" height="94" fill="#3f86d0"/>
    <path d="M145 80V70M135 78l10-12 10 12" stroke="#1f5aa8" stroke-width="4" fill="none"/>
  </svg>
  <div class="txt" style="left:200px;top:80px;width:130px">Add your agenda point here<br>Add your agenda point here<br>Add your agenda point here</div>
  <div class="footer"><span class="brand">Bright Towns Alliance</span><span class="meta">Add footer note</span></div>
</section>
<section class="slide c2" style="top:465px">
  <div class="title">Progressive Agenda</div>
  <div class="photo ph-skyline" style="left:20px;right:20px;top:95px;bottom:15px" role="img" aria-label="Green city skyline illustration"></div>
  <svg width="346" height="195" viewBox="0 0 346 195">
    <circle cx="93" cy="62" r="9" fill="#f39a1e"/><circle cx="133" cy="62" r="9" fill="#f39a1e"/><circle cx="173" cy="62" r="9" fill="#f39a1e"/>
    <circle cx="213" cy="62" r="9" fill="#f39a1e"/><circle cx="253" cy="62" r="9" fill="#f39a1e"/>
  </svg>
  <div class="footer"><span class="brand">Bright Towns Alliance</span><span class="meta">Add footer note</span></div>
</section>

<!-- Row 4 -->
<section class="slide c1 section" style="top:689px;background:linear-gradient(135deg,#1f5aa8,#123f85)">
  <div class="label">Full Bleed With Picture Banners<small>Slide Notes</small></div>
</section>
<section class="slide c2" style="top:689px">
  <div class="photo ph-crowd" style="inset:0" role="img" aria-label="Black and white photograph of a conference audience"></div>
  <div class="banner" style="left:0;right:0;top:8px">Enter Your Slide Title Text Here</div>
</section>
<section class="slide c3" style="top:689px">
  <div class="photo ph-crowd-c" style="inset:0" role="img" aria-label="Photograph of a conference hall audience"></div>
  <div class="banner" style="left:6px;width:106px;top:8px">Your Banner Title</div>
  <div class="banner" style="left:120px;width:106px;top:8px">Your Banner Title</div>
  <div class="banner" style="left:234px;width:106px;top:8px">Your Banner Title</div>
</section>

<!-- Row 5 -->
<section class="slide c1" style="top:906px">
  <div class="photo ph-city" style="inset:0" role="img" aria-label="City photograph in dark blue tones"></div>
  <div class="big" style="position:absolute;left:0;right:0;top:66px;text-align:center;font-size:14px;line-height:1.3">Citizens increasingly expect<br>their cities to be<br><span class="accent">fully digital</span></div>
</section>
<section class="slide c2 section" style="top:906px;background:linear-gradient(135deg,#163776,var(--navy))">
  <div class="label">3 Quotation<small>Slide Notes</small></div>
</section>
<section class="slide c3" style="top:906px">
  <div class="photo ph-portrait" style="inset:0" role="img" aria-label="Portrait photograph of a speaker"></div>
  <div class="txt w" style="left:14px;top:50px;width:120px;font-size:5.5px">“For those of us living in cities, we need to make sure that we benefit from this change.”</div>
  <div class="txt w" style="left:14px;top:110px;font-weight:700">Speaker Name<br><span style="font-weight:400">Role and Organisation</span></div>
  <div class="footer"><span class="brand">Bright Towns Alliance</span><span class="meta">Add footer note</span></div>
</section>

<!-- Row 6 -->
<section class="slide c1" style="top:1126px">
  <div class="photo ph-portrait" style="inset:0" role="img" aria-label="Portrait photograph of a speaker"></div>
  <div class="txt w" style="left:14px;top:36px;width:120px;font-size:5.5px">“For those of us living in cities, we need to make sure that we benefit from this change.”</div>
  <div class="txt" style="left:14px;top:80px;width:120px;color:var(--orange)">Add a second line of quotation text here</div>
  <div class="txt w" style="left:14px;top:115px;font-weight:700">Speaker Name<br><span style="font-weight:400">Role and Organisation</span></div>
  <div class="footer"><span class="brand">Bright Towns Alliance</span><span class="meta">Add footer note</span></div>
</section>
<section class="slide c2" style="top:1126px">
  <div class="photo ph-portrait" style="inset:0" role="img" aria-label="Portrait photograph of a speaker"></div>
  <div class="txt w" style="left:14px;top:40px;width:120px;font-size:5.5px">“For those of us living in cities, we need to make sure that we benefit from this change.”</div>
  <div class="txt w" style="left:14px;top:95px;font-weight:700">Speaker Name<br><span style="font-weight:400">Role and Organisation</span></div>
  <div class="footer"><span class="brand">Bright Towns Alliance</span><span class="meta">Add footer note</span></div>
</section>

<!-- Row 7 -->
<section class="slide c1 section" style="top:1356px;background:linear-gradient(135deg,#1f5aa8,#123f85)">
  <div class="label">4 Text-Heavy With Complementary Picture<small>Slide Notes</small></div>
</section>
<section class="slide c2" style="top:1356px">
  <div class="title">Your Slide Title Here</div>
  <svg width="346" height="195" viewBox="0 0 346 195">
    <circle cx="30" cy="70" r="6" fill="#e9532b"/><circle cx="60" cy="70" r="6" fill="#f39a1e"/><circle cx="90" cy="70" r="6" fill="#5f9e37"/><circle cx="120" cy="70" r="6" fill="#3f86d0"/><circle cx="150" cy="70" r="6" fill="#1f5aa8"/>
  </svg>
  <div class="txt" style="left:22px;top:90px;width:150px">Add supporting body text here to explain the main idea of this slide in a few short lines.</div>
  <div class="photo ph-crowd-c" style="left:185px;top:40px;width:145px;height:125px" role="img" aria-label="Photograph of a conference audience"></div>
  <div class="footer"><span class="brand">Bright Towns Alliance</span><span class="meta">Add footer note</span></div>
</section>
<section class="slide c3" style="top:1356px">
  <div class="title left">Your Slide Title Here</div>
  <div class="txt" style="left:20px;top:45px;width:150px">Add supporting body text here to explain the main idea of this slide in a few short lines.<br><br>• First point to make<br>• Second point to make<br>• Third point to make</div>
  <div class="photo ph-crowd" style="left:185px;top:0;width:161px;height:180px" role="img" aria-label="Black and white photograph of an audience"></div>
  <div class="footer"><span class="brand">Bright Towns Alliance</span><span class="meta">Add footer note</span></div>
</section>

<!-- Row 8 -->
<section class="slide c1" style="top:1570px">
  <div class="title left">Your Slide Title Here</div>
  <div class="txt" style="left:20px;top:45px;width:150px">• First point to make<br>• Second point to make<br>• Third point to make<br>• Fourth point to make<br>• Fifth point to make</div>
  <div class="photo ph-crowd-c" style="left:185px;top:0;width:161px;height:100px" role="img" aria-label="Photograph of a conference audience"></div>
  <div class="txt" style="left:190px;top:110px;width:140px">Add a short caption here.</div>
  <div class="footer"><span class="brand">Bright Towns Alliance</span><span class="meta">Add footer note</span></div>
</section>
<section class="slide c2" style="top:1570px">
  <div class="title">Your Slide Title Here</div>
  <div class="txt" style="left:20px;top:45px;width:150px">• First point to make<br>• Second point to make<br>• Third point to make<br>• Fourth point to make</div>
  <div class="photo ph-crowd" style="left:185px;top:40px;width:145px;height:125px" role="img" aria-label="Black and white photograph of a panel discussion"></div>
  <div class="footer"><span class="brand">Bright Towns Alliance</span><span class="meta">Add footer note</span></div>
</section>
<section class="slide c3" style="top:1570px">
  <div class="photo ph-crowd-c" style="left:0;top:0;width:346px;height:85px" role="img" aria-label="Photograph of a large conference audience"></div>
  <div class="title" style="top:92px">Your Slide Title Here</div>
  <div class="txt" style="left:20px;top:120px;width:300px">Add supporting body text here to explain the main idea of this slide in a few short lines.</div>
  <div class="footer"><span class="brand">Bright Towns Alliance</span><span class="meta">Add footer note</span></div>
</section>

<!-- Row 9 -->
<section class="slide c1 section" style="top:1800px;background:linear-gradient(135deg,#ef6a3b,var(--red))">
  <div class="label">5 Statistics Heavy<small>Slide Notes</small></div>
</section>
<section class="slide c2" style="top:1800px">
  <div class="title">Your Slide Title Here</div>
  <div style="position:absolute;left:25px;top:45px;font-size:20px;font-weight:700;color:var(--blue)">66%</div>
  <svg width="346" height="195" viewBox="0 0 346 195">
    <rect x="25" y="80" width="120" height="4" fill="#e6e9ee"/><rect x="25" y="80" width="80" height="4" fill="#5f9e37"/>
    <rect x="25" y="100" width="120" height="4" fill="#e6e9ee"/><rect x="25" y="100" width="60" height="4" fill="#f39a1e"/>
    <rect x="25" y="120" width="120" height="4" fill="#e6e9ee"/><rect x="25" y="120" width="95" height="4" fill="#1f5aa8"/>
  </svg>
  <div class="txt" style="left:175px;top:45px;width:150px">Add supporting body text here to explain each statistic and where the numbers come from.</div>
  <div class="footer"><span class="brand">Bright Towns Alliance</span><span class="meta">Add footer note</span></div>
</section>
<section class="slide c3" style="top:1800px">
  <div class="photo ph-pink" style="inset:0" role="img" aria-label="Audience photograph with pink overlay"></div>
  <div class="title light">Your Slide Title Here</div>
  <div class="stat" style="left:20px;top:80px"><b>101</b><span>Add label</span></div>
  <div class="stat" style="left:100px;top:80px"><b>25150</b><span>Add label</span></div>
  <div class="stat" style="left:180px;top:80px"><b>672</b><span>Add label</span></div>
  <div class="stat" style="left:260px;top:80px"><b>980</b><span>Add label</span></div>
  <div class="footer"><span class="brand">Bright Towns Alliance</span><span class="meta">Add footer note</span></div>
</section>

<!-- Row 10 -->
<section class="slide c1" style="top:2011px">
  <div class="photo ph-pink" style="inset:0" role="img" aria-label="Audience photograph with pink overlay"></div>
  <div class="title light">Your Slide Title Here</div>
  <div class="stat" style="left:20px;top:70px"><b>101</b><span>Add label</span></div>
  <div class="stat" style="left:100px;top:70px"><b>25150</b><span>Add label</span></div>
  <div class="stat" style="left:180px;top:70px"><b>672</b><span>Add label</span></div>
  <div class="stat" style="left:260px;top:70px"><b>980</b><span>Add label</span></div>
  <div class="footer"><span class="brand">Bright Towns Alliance</span><span class="meta">Add footer note</span></div>
</section>

<!-- Row 11 -->
<section class="slide c1 section" style="top:2244px;background:linear-gradient(135deg,#f6ac3c,var(--orange))">
  <div class="label">6 World Map<small>Slide Notes</small></div>
</section>
<section class="slide c2" style="top:2244px">
  <div class="title">Your Slide Title Here</div>
  <div class="photo ph-map" style="left:40px;top:42px;width:266px;height:125px" role="img" aria-label="World map in light grey"></div>
  <div class="footer"><span class="brand">Bright Towns Alliance</span><span class="meta">Add footer note</span></div>
</section>
<section class="slide c3" style="top:2244px">
  <div class="title">Your Slide Title Here</div>
  <div class="photo ph-map" style="left:15px;top:42px;width:205px;height:120px" role="img" aria-label="World map in light grey"></div>
  <div class="txt" style="left:232px;top:55px;width:100px">Add supporting text about the regions shown on the map.</div>
  <div class="footer"><span class="brand">Bright Towns Alliance</span><span class="meta">Add footer note</span></div>
</section>

<!-- Row 12 -->
<section class="slide c1" style="top:2458px;background:var(--navy)">
  <div class="title light">Your Slide Title Here</div>
  <div class="photo ph-map dark" style="left:40px;top:42px;width:266px;height:125px" role="img" aria-label="World map in white on navy"></div>
  <div class="footer"><span class="brand">Bright Towns Alliance</span><span class="meta">Add footer note</span></div>
</section>
<section class="slide c2" style="top:2458px;background:var(--navy)">
  <div class="title light">Your Slide Title Here</div>
  <div class="txt w" style="left:30px;top:40px;width:286px">Add supporting text about the regions shown on the map below.</div>
  <div class="photo ph-map dark" style="left:60px;top:62px;width:226px;height:108px" role="img" aria-label="World map in white on navy"></div>
  <div class="footer"><span class="brand">Bright Towns Alliance</span><span class="meta">Add footer note</span></div>
</section>

<!-- Row 13 -->
<section class="slide c1 section" style="top:2675px;background:linear-gradient(135deg,#72b04a,var(--green))">
  <div class="label">7 Two Column Table<small>Slide Notes</small></div>
</section>
<section class="slide c2" style="top:2675px">
  <div class="title">Two Column Table Only</div>
  <table class="tbl" style="left:30px;top:40px;width:286px">
    <tr><th>Column header</th><th>Column header</th></tr>
    <tr><td>Add text here</td><td>Add text here</td></tr><tr><td>Add text here</td><td>Add text here</td></tr>
    <tr><td>Add text here</td><td>Add text here</td></tr><tr><td>Add text here</td><td>Add text here</td></tr>
    <tr><td>Add text here</td><td>Add text here</td></tr><tr><td>Add text here</td><td>Add text here</td></tr>
  </table>
  <div class="footer"><span class="brand">Bright Towns Alliance</span><span class="meta">Add footer note</span></div>
</section>
<section class="slide c3" style="top:2675px">
  <div class="title">Two Column Table With Image</div>
  <table class="tbl" style="left:15px;top:40px;width:185px">
    <tr><th>Header</th><th>Header</th></tr>
    <tr><td>Add text</td><td>Add text</td></tr><tr><td>Add text</td><td>Add text</td></tr>
    <tr><td>Add text</td><td>Add text</td></tr><tr><td>Add text</td><td>Add text</td></tr>
    <tr><td>Add text</td><td>Add text</td></tr>
  </table>
  <div class="photo ph-crowd" style="left:210px;top:40px;width:125px;height:125px" role="img" aria-label="Black and white photograph of an audience"></div>
  <div class="footer"><span class="brand">Bright Towns Alliance</span><span class="meta">Add footer note</span></div>
</section>

<!-- Row 14 -->
<section class="slide c1 section" style="top:2908px;background:linear-gradient(135deg,#8a8a8a,var(--gray))">
  <div class="label">8 2 Pictures<small>Slide Notes</small></div>
</section>
<section class="slide c2" style="top:2908px">
  <div class="title">Two Pictures Slide</div>
  <div class="photo ph-crowd-c" style="left:20px;top:42px;width:148px;height:95px" role="img" aria-label="Photograph of a conference audience"></div>
  <div class="photo ph-crowd" style="left:178px;top:42px;width:148px;height:95px" role="img" aria-label="Black and white photograph of a panel"></div>
  <div class="txt" style="left:20px;top:145px">Add caption here</div><div class="txt" style="left:178px;top:145px">Add caption here</div>
  <div class="footer"><span class="brand">Bright Towns Alliance</span><span class="meta">Add footer note</span></div>
</section>
<section class="slide c3" style="top:2908px">
  <div class="photo ph-crowd-c" style="left:0;top:0;width:173px;height:195px" role="img" aria-label="Photograph of a conference audience"></div>
  <div class="photo ph-crowd" style="left:173px;top:0;width:173px;height:195px" role="img" aria-label="Black and white photograph of an audience"></div>
  <div class="banner blue" style="left:0;right:0;bottom:10px">Enter Your Callout Banner Text Here</div>
</section>

<!-- Row 15 -->
<section class="slide c1" style="top:3122px">
  <div class="photo ph-crowd-c" style="inset:0" role="img" aria-label="Photograph of a large conference audience"></div>
  <div class="banner" style="left:10px;top:10px;padding:5px 12px">Your Title Here</div>
  <div class="banner blue" style="left:0;right:0;bottom:10px">Enter Your Callout Banner Text Here</div>
</section>

<!-- Row 16 -->
<section class="slide c1 section" style="top:3358px;background:linear-gradient(135deg,#8a8a8a,var(--gray))">
  <div class="label">9 Timeline<small>Slide Notes</small></div>
</section>
<section class="slide c2" style="top:3358px">
  <div class="title">Six Months Timeline</div>
  <svg width="346" height="195" viewBox="0 0 346 195">
    <line x1="30" y1="100" x2="316" y2="100" stroke="#d9dde3" stroke-width="2"/>
    <circle cx="55" cy="100" r="7" fill="#7a3fa6"/><circle cx="103" cy="100" r="7" fill="#f39a1e"/><circle cx="151" cy="100" r="7" fill="#5f9e37"/>
    <circle cx="199" cy="100" r="7" fill="#3f86d0"/><circle cx="247" cy="100" r="7" fill="#e9532b"/><circle cx="295" cy="100" r="7" fill="#1f5aa8"/>
  </svg>
  <div class="txt" style="left:40px;top:78px">Month one</div><div class="txt" style="left:136px;top:78px">Month three</div><div class="txt" style="left:232px;top:78px">Month five</div>
  <div class="txt" style="left:88px;top:113px">Month two</div><div class="txt" style="left:184px;top:113px">Month four</div><div class="txt" style="left:282px;top:113px">Month six</div>
  <div class="footer"><span class="brand">Bright Towns Alliance</span><span class="meta">Add footer note</span></div>
</section>
<section class="slide c3" style="top:3358px">
  <div class="title">One Year Timeline</div>
  <svg width="346" height="195" viewBox="0 0 346 195">
    <line x1="25" y1="140" x2="321" y2="140" stroke="#9aa3ad" stroke-width="1"/>
    <rect x="45" y="90" width="3" height="50" fill="#1f5aa8"/><rect x="85" y="105" width="3" height="35" fill="#f39a1e"/>
    <rect x="125" y="80" width="3" height="60" fill="#e9532b"/><rect x="165" y="100" width="3" height="40" fill="#1f5aa8"/>
    <rect x="205" y="70" width="3" height="70" fill="#f39a1e"/><rect x="245" y="95" width="3" height="45" fill="#1f5aa8"/>
    <rect x="285" y="85" width="3" height="55" fill="#e9532b"/>
  </svg>
  <div class="footer"><span class="brand">Bright Towns Alliance</span><span class="meta">Add footer note</span></div>
</section>

<!-- Row 17 -->
<section class="slide c1" style="top:3572px;background:#1f2a3e">
  <div class="title light left">Key Events Timeline</div>
  <svg width="346" height="195" viewBox="0 0 346 195">
    <line x1="20" y1="45" x2="326" y2="45" stroke="#56617a"/>
    <rect x="60" y="55" width="70" height="4" fill="#f39a1e"/><rect x="110" y="67" width="90" height="4" fill="#3f86d0"/>
    <rect x="150" y="79" width="60" height="4" fill="#5f9e37"/><rect x="190" y="91" width="80" height="4" fill="#e9532b"/>
    <rect x="230" y="103" width="70" height="4" fill="#7a3fa6"/>
  </svg>
  <div class="txt w" style="left:20px;top:125px;width:300px">Add event descriptions here.</div>
  <div class="footer"><span class="brand">Bright Towns Alliance</span><span class="meta">Add footer note</span></div>
</section>
<section class="slide c2" style="top:3572px">
  <div class="title">Key Events Timeline</div>
  <svg width="346" height="195" viewBox="0 0 346 195">
    <line x1="20" y1="55" x2="326" y2="55" stroke="#d9dde3"/>
    <rect x="50" y="70" width="90" height="5" fill="#1f5aa8"/><rect x="120" y="82" width="110" height="5" fill="#5f9e37"/>
    <rect x="90" y="94" width="80" height="5" fill="#e9532b"/><rect x="180" y="106" width="120" height="5" fill="#f39a1e"/>
    <rect x="150" y="118" width="70" height="5" fill="#3f86d0"/>
  </svg>
  <div class="footer"><span class="brand">Bright Towns Alliance</span><span class="meta">Add footer note</span></div>
</section>

<!-- Row 18 -->
<section class="slide c1 section" style="top:3823px;background:linear-gradient(135deg,#1f5aa8,#123f85)">
  <div class="label">10 Linear Progress<small>Slide Notes</small></div>
</section>
<section class="slide c2" style="top:3823px">
  <div class="title">Your Slide Title</div>
  <svg width="346" height="195" viewBox="0 0 346 195">
    <circle cx="60" cy="70" r="9" fill="#1f5aa8"/><circle cx="60" cy="100" r="9" fill="#3f86d0"/><circle cx="60" cy="130" r="9" fill="#1f5aa8"/>
    <circle cx="190" cy="70" r="9" fill="#3f86d0"/><circle cx="190" cy="100" r="9" fill="#1f5aa8"/><circle cx="190" cy="130" r="9" fill="#3f86d0"/>
  </svg>
  <div class="txt" style="left:75px;top:66px">Add text here</div><div class="txt" style="left:75px;top:96px">Add text here</div><div class="txt" style="left:75px;top:126px">Add text here</div>
  <div class="txt" style="left:205px;top:66px">Add text here</div><div class="txt" style="left:205px;top:96px">Add text here</div><div class="txt" style="left:205px;top:126px">Add text here</div>
  <div class="footer"><span class="brand">Bright Towns Alliance</span><span class="meta">Add footer note</span></div>
</section>
<section class="slide c3" style="top:3823px">
  <div class="title">Your Slide Title</div>
  <svg width="346" height="195" viewBox="0 0 346 195">
    <rect x="40" y="55" width="55" height="55" fill="#1f5aa8"/><rect x="112" y="55" width="55" height="55" fill="#f39a1e"/>
    <rect x="184" y="55" width="55" height="55" fill="#7a7a7a"/><rect x="256" y="55" width="55" height="55" fill="#e9532b"/>
  </svg>
  <div class="txt" style="left:40px;top:120px">Add text</div><div class="txt" style="left:112px;top:120px">Add text</div><div class="txt" style="left:184px;top:120px">Add text</div><div class="txt" style="left:256px;top:120px">Add text</div>
  <div class="footer"><span class="brand">Bright Towns Alliance</span><span class="meta">Add footer note</span></div>
</section>

<!-- Row 19 -->
<section class="slide c1" style="top:4038px">
  <div class="title">Your Slide Title</div>
  <svg width="346" height="195" viewBox="0 0 346 195">
    <line x1="50" y1="90" x2="296" y2="90" stroke="#d9dde3" stroke-width="2"/>
    <circle cx="60" cy="90" r="18" fill="#1f5aa8"/><circle cx="135" cy="90" r="18" fill="#3f86d0"/>
    <circle cx="210" cy="90" r="18" fill="#f39a1e"/><circle cx="285" cy="90" r="18" fill="#e9532b"/>
  </svg>
  <div class="txt" style="left:50px;top:125px">Add text</div><div class="txt" style="left:125px;top:125px">Add text</div><div class="txt" style="left:200px;top:125px">Add text</div><div class="txt" style="left:275px;top:125px">Add text</div>
  <div class="footer"><span class="brand">Bright Towns Alliance</span><span class="meta">Add footer note</span></div>
</section>
<section class="slide c2" style="top:4038px">
  <div class="title">Your Slide Title</div>
  <svg width="346" height="195" viewBox="0 0 346 195">
    <circle cx="110" cy="80" r="22" fill="#1f5aa8" opacity=".9"/><circle cx="140" cy="80" r="22" fill="#5f9e37" opacity=".9"/>
    <circle cx="110" cy="110" r="22" fill="#f39a1e" opacity=".9"/><circle cx="140" cy="110" r="22" fill="#e9532b" opacity=".9"/>
    <circle cx="125" cy="95" r="12" fill="#ffffff"/>
  </svg>
  <div class="txt" style="left:190px;top:70px;width:130px">Add text here<br><br>Add text here<br><br>Add text here</div>
  <div class="footer"><span class="brand">Bright Towns Alliance</span><span class="meta">Add footer note</span></div>
</section>
<section class="slide c3" style="top:4038px">
  <div class="title">Your Slide Title</div>
  <svg width="346" height="195" viewBox="0 0 346 195">
    <g fill="none" stroke-width="16">
      <path d="M173 60a40 40 0 0 1 38 28" stroke="#1f5aa8"/><path d="M211 88a40 40 0 0 1-14 43" stroke="#f39a1e"/>
      <path d="M197 131a40 40 0 0 1-48 0" stroke="#5f9e37"/><path d="M149 131a40 40 0 0 1-14-43" stroke="#e9532b"/>
      <path d="M135 88a40 40 0 0 1 38-28" stroke="#7a3fa6"/>
    </g>
  </svg>
  <div class="txt" style="left:20px;top:70px">Add text</div><div class="txt" style="left:290px;top:70px">Add text</div>
  <div class="txt" style="left:20px;top:130px">Add text</div><div class="txt" style="left:290px;top:130px">Add text</div>
  <div class="footer"><span class="brand">Bright Towns Alliance</span><span class="meta">Add footer note</span></div>
</section>

<!-- Row 20 -->
<section class="slide c1" style="top:4252px">
  <div class="title">Your Slide Title</div>
  <svg width="346" height="195" viewBox="0 0 346 195">
    <g fill="none" stroke-width="6">
      <circle cx="60" cy="95" r="20" stroke="#1f5aa8"/><circle cx="105" cy="95" r="20" stroke="#3f86d0"/>
      <circle cx="150" cy="95" r="20" stroke="#5f9e37"/><circle cx="195" cy="95" r="20" stroke="#f39a1e"/>
      <circle cx="240" cy="95" r="20" stroke="#e9532b"/><circle cx="285" cy="95" r="20" stroke="#7a3fa6"/>
    </g>
  </svg>
  <div class="txt" style="left:40px;top:130px;width:270px">Add short text under each step of the process.</div>
  <div class="footer"><span class="brand">Bright Towns Alliance</span><span class="meta">Add footer note</span></div>
</section>
<section class="slide c2" style="top:4252px">
  <div class="title">Your Slide Title</div>
  <svg width="346" height="195" viewBox="0 0 346 195">
    <path d="M40 110a25 25 0 0 1 50 0a25 25 0 0 0 50 0a25 25 0 0 1 50 0a25 25 0 0 0 50 0a25 25 0 0 1 50 0" fill="none" stroke="#d9dde3" stroke-width="6"/>
    <circle cx="65" cy="85" r="10" fill="#1f5aa8"/><circle cx="115" cy="135" r="10" fill="#f39a1e"/>
    <circle cx="165" cy="85" r="10" fill="#5f9e37"/><circle cx="215" cy="135" r="10" fill="#e9532b"/><circle cx="265" cy="85" r="10" fill="#3f86d0"/>
  </svg>
  <div class="footer"><span class="brand">Bright Towns Alliance</span><span class="meta">Add footer note</span></div>
</section>
<section class="slide c3" style="top:4252px">
  <div class="title">Your Slide Title</div>
  <svg width="346" height="195" viewBox="0 0 346 195">
    <rect x="80" y="50" width="26" height="26" fill="#1f5aa8"/><rect x="112" y="50" width="26" height="26" fill="#e9532b"/>
    <rect x="80" y="82" width="26" height="26" fill="#f39a1e"/><rect x="112" y="82" width="26" height="26" fill="#1f5aa8"/>
    <rect x="80" y="114" width="26" height="26" fill="#e9532b"/><rect x="112" y="114" width="26" height="26" fill="#f39a1e"/>
  </svg>
  <div class="txt" style="left:160px;top:55px;width:150px">Add text here<br><br>Add text here<br><br>Add text here</div>
  <div class="footer"><span class="brand">Bright Towns Alliance</span><span class="meta">Add footer note</span></div>
</section>

</body>
</html>
```